Renewed electronic office supplies

I need a landing page design for a B2B business that will sell refurbished and renewed electronic devices such as smartphones, laptops, tablets and other gadgets. We want to become suppliers of these devices to companies that need computers and other devices for their employees. The point of our business is that they can get a great device that is in very good contrition instead of buying brand new. Companies will be able to save 50-60% on these renewed devices. Not only that we will also buy the companies old devices which they no longe needs and renew them and give them new life so we can resell it.

Our services will be:

- sale of renewed devices with lifetime warranty

- purchase of old devices

- swap solution: meaning client buy from us and sell at the same time so we deduct the amount sale of their old devices into their purchase.

Some useful information:

- company name and logo are still pending

- we aim to provide all business with top quality of renewed and environmentally friendly electronics, while maintaining a minimal impact on the natural environment.

I have attached a word document with some additional info that might be useful

Looking forward to seeing all your great designs!

P.s. Please feel free to make designs that are not based on my documents also, we need different layouts and designs. as for now I see many of the designs are more or less the same. we need more variation on design
Updates

Target Market(s)

Medium to large Businesses

Industry/Entity Type

Technology Equipment

Requirements
Must have
• we need more designs to be submitted , 50 designs minimum

```html
<!DOCTYPE html>
<html lang="en">
<head>
<meta charset="UTF-8">
<title>Reusable Electronic Office Supplies</title>
<link rel="stylesheet" href="https://fonts.googleapis.com/css2?family=Bebas+Neue&family=Montserrat:wght@400;500;800;900&display=swap">
<style>
  :root {
    --blue: #3f6cf2;
    --blue-deep: #3459d6;
    --blue-band: #3a63e0;
    --green: #68b531;
    --navy: #0f1f5c;
    --heading-blue: #2f5ae0;
    --numeral-top: #a9bcf2;
    --numeral-bottom: #eef2fc;
    --white: #ffffff;
    --ink: #111111;
  }
  * { margin: 0; padding: 0; box-sizing: border-box; }
  html, body { width: 738px; height: 1200px; overflow: hidden; background: var(--white); }
  body { font-family: 'Montserrat', sans-serif; color: var(--ink); position: relative; }

  .hero {
    position: absolute; left: 0; top: 0; width: 738px; height: 358px;
    background: linear-gradient(135deg, #4676f8 0%, var(--blue) 50%, var(--blue-deep) 100%);
  }
  .brand { font-family: 'Bebas Neue', sans-serif; color: var(--white); letter-spacing: 0.3px; }
  .hero .brand { position: absolute; left: 149px; top: 15px; font-size: 14px; }
  .social { position: absolute; display: flex; gap: 4px; }
  .social span { width: 12px; height: 12px; border-radius: 50%; background: rgba(255,255,255,0.55); display: block; }
  .hero .social { left: 413px; top: 16px; }
  .phone-number { position: absolute; color: var(--white); font-size: 9.5px; letter-spacing: 0.2px; }
  .hero .phone-number { left: 491px; top: 16px; }

  .hero-title {
    position: absolute; left: 149px; top: 128px;
    font-family: 'Bebas Neue', sans-serif; font-size: 34px; line-height: 27px;
    background: linear-gradient(180deg, #ffffff 0%, #e4ebff 45%, #9fb6f7 100%);
    -webkit-background-clip: text; background-clip: text; color: transparent;
  }
  .hero-text { position: absolute; left: 150px; top: 195px; width: 215px; color: var(--white); font-size: 7px; line-height: 9.8px; }
  .shop-button {
    position: absolute; left: 150px; top: 240px; width: 130px; height: 33px;
    background: var(--green); border-radius: 6px; color: var(--white);
    font-size: 15px; letter-spacing: 0.5px; display: flex; align-items: center; justify-content: center;
  }
  .device-mockup {
    position: absolute; left: 338px; top: 115px; width: 262px; height: 192px;
    background: radial-gradient(ellipse at 60% 45%, #c9ccd6 0%, #8d9ee0 40%, rgba(63,108,242,0) 72%);
  }

  .categories { position: absolute; left: 0; top: 358px; width: 738px; height: 191px; display: flex; }
  .category { width: 25%; height: 100%; display: flex; flex-direction: column; }
  .category-photo { height: 145px; }
  .category-label {
    flex: 1; background: var(--blue-band); color: var(--white);
    font-family: 'Bebas Neue', sans-serif; font-size: 22px;
    display: flex; align-items: center; justify-content: center;
  }
  .category.is-active .category-label { background: var(--green); }
  .photo-grey-a { background: linear-gradient(135deg, #6d6d6d, #c4c4c4 60%, #8a8a8a); }
  .photo-grey-b { background: linear-gradient(135deg, #9a9a9a, #d6d6d6 50%, #6e6e6e); }
  .photo-tinted { background: linear-gradient(160deg, #3a8fd8 0%, #4fc9a8 40%, #7be04a 75%, #3d8c22 100%); }
  .photo-grey-c { background: linear-gradient(135deg, #5a5a5a, #b8b8b8 55%, #d9d9d9); }

  .about-title {
    position: absolute; left: 0; top: 612px; width: 738px; text-align: center;
    font-family: 'Bebas Neue', sans-serif; font-size: 40px; line-height: 40px;
    background: linear-gradient(180deg, #0a1436, #1c3a9e);
    -webkit-background-clip: text; background-clip: text; color: transparent;
  }
  .about-title-wrap { position: absolute; left: 0; top: 612px; width: 738px; display: flex; justify-content: center; }
  .about-title-wrap .about-title { position: static; width: auto; }

  .step { position: absolute; }
  .step-numeral {
    position: absolute; font-weight: 900; line-height: 1;
    background: linear-gradient(180deg, var(--numeral-top), var(--numeral-bottom));
    -webkit-background-clip: text; background-clip: text; color: transparent;
  }
  .step-heading { color: var(--heading-blue); font-weight: 800; font-size: 11px; line-height: 13.5px; letter-spacing: 0.2px; }
  .step-text { font-size: 9px; line-height: 11px; color: var(--ink); }

  .step-one .step-numeral { left: 140px; top: 662px; font-size: 132px; }
  .step-one .step-body { position: absolute; left: 216px; top: 684px; width: 330px; }
  .step-two .step-numeral { left: 222px; top: 790px; font-size: 134px; }
  .step-two .step-body { position: absolute; left: 326px; top: 817px; width: 165px; }
  .step-three .step-numeral { left: 334px; top: 920px; font-size: 134px; }
  .step-three .step-body { position: absolute; left: 430px; top: 946px; width: 160px; }

  .footer {
    position: absolute; left: 0; top: 1104px; width: 738px; height: 96px;
    background: linear-gradient(135deg, #4676f8 0%, var(--blue) 50%, var(--blue-deep) 100%);
  }
  .footer .brand { position: absolute; left: 149px; top: 28px; font-size: 25px; }
  .footer .phone-number { left: 497px; top: 32px; }
  .footer .social { left: 526px; top: 48px; }
  .footer .social span { background: var(--white); }
</style>
</head>
<body>
  <header class="hero">
    <div class="brand">COMPANYNAME</div>
    <div class="social" aria-label="Social links"><span></span><span></span><span></span><span></span></div>
    <div class="phone-number">+00-00000000000</div>
    <h1 class="hero-title">REUSABLE ELECTRONIC<br>OFFICE SUPPLIES</h1>
    <p class="hero-text">We aim to provide all business with top quality of reused and environmentally friendly electronics, while maintaining a minimal impact on the natural environment.</p>
    <div class="shop-button">SHOP</div>
    <div class="device-mockup" role="img" aria-label="Blue laptop with a smartphone leaning on its screen"></div>
  </header>

  <section class="categories">
    <div class="category">
      <div class="category-photo photo-grey-a" role="img" aria-label="Hands repairing a smartphone"></div>
      <div class="category-label">SMARTPHONES</div>
    </div>
    <div class="category">
      <div class="category-photo photo-grey-b" role="img" aria-label="Technician repairing a laptop board under a magnifier"></div>
      <div class="category-label">LAPTOPS</div>
    </div>
    <div class="category is-active">
      <div class="category-photo photo-tinted" role="img" aria-label="Technician replacing a tablet screen"></div>
      <div class="category-label">TABLETS</div>
    </div>
    <div class="category">
      <div class="category-photo photo-grey-c" role="img" aria-label="Hands fixing a small gadget"></div>
      <div class="category-label">GADGETS</div>
    </div>
  </section>

  <div class="about-title-wrap"><h2 class="about-title">WE ARE</h2></div>

  <section class="step step-one">
    <div class="step-numeral">1</div>
    <div class="step-body">
      <h3 class="step-heading">A SMARTER CIRCULAR SOLUTION<br>FOR ELECTRONIC SUPPLIES</h3>
      <p class="step-text">Billions of electronics are being made, sold, and disposed of every year – a cycle that drives short-term profits for electronics manufacturers, but at too high a cost for the planet we all share. With our experience in the recycling market we can put an end to this cycle and offer a circular solution that is both affordable and environmentally friendly.</p>
    </div>
  </section>

  <section class="step step-two">
    <div class="step-numeral">2</div>
    <div class="step-body">
      <h3 class="step-heading">BUY REUSABLE IT</h3>
      <p class="step-text">We specialize in refurbished electronic devices with top quality for affordable prices.<br>All our products have undergone a detailed testing and reconditioning program by expert technicians.</p>
    </div>
  </section>

  <section class="step step-three">
    <div class="step-numeral">3</div>
    <div class="step-body">
      <h3 class="step-heading">SELL YOUR IT SAFELY</h3>
      <p class="step-text">We can also buy your used electronics and make sure they get reused and give them a new life. By selling your used devices that you no longer have use for you can help us create carbon savings</p>
    </div>
  </section>

  <footer class="footer">
    <div class="brand">COMPANYNAME</div>
    <div class="phone-number">+00-10025000000</div>
    <div class="social" aria-label="Social links"><span></span><span></span><span></span><span></span></div>
  </footer>
</body>
</html>
```